Organic Mavu (Coffee) Scrub Label for high end product

Need a product label for a coffee based body scrub called Mavu Body Scrub a 100% organic product. Our primary target is the yoga community so designs should reflect calm, perhaps incorporate eastern yoga symbology. simpler the better. Design should include both a round lid label and a rectangular wrap around label.

Target Market(s)

yoga community, people with cellulite, etc.

Industry/Entity Type

Community

```html
<!DOCTYPE html>
<html lang="en">
<head>
<meta charset="utf-8">
<title>Mavu Body Scrub – Lid Label</title>
<link rel="stylesheet" href="https://fonts.googleapis.com/css2?family=Josefin+Sans:wght@300&family=Italianno&display=swap">
<style>
  :root {
    --page: #ffffff;
    --grounds-light: #6a3526;
    --grounds-mid: #3f1e14;
    --grounds-deep: #1f0e09;
    --band-line: #7a4a30;
    --gold-light: #fbe27a;
    --gold-deep: #d9a521;
    --label-white: #ffffff;
    --wordmark: #a87a4c;
    --maroon: #5a1414;
    --chevron-tan: #d6b896;
  }
  html, body {
    margin: 0;
    padding: 0;
    width: 1200px;
    height: 1200px;
    overflow: hidden;
    background: var(--page);
  }
  .lid-label {
    display: block;
    width: 1200px;
    height: 1200px;
  }
  .tagline {
    font-family: "Italianno", cursive;
    font-size: 64px;
    fill: var(--maroon);
  }
  .brand-name {
    font-family: "Josefin Sans", sans-serif;
    font-weight: 300;
    font-size: 206px;
    fill: var(--wordmark);
  }
  .product-type {
    font-family: "Josefin Sans", sans-serif;
    font-weight: 300;
    font-size: 44px;
    fill: var(--maroon);
  }
</style>
</head>
<body>
<svg class="lid-label" viewBox="0 0 1200 1200" xmlns="http://www.w3.org/2000/svg">
  <defs>
    <linearGradient id="grounds-tone" x1="0" y1="0" x2="0" y2="1">
      <stop offset="0" stop-color="var(--grounds-light)"/>
      <stop offset="0.45" stop-color="var(--grounds-mid)"/>
      <stop offset="1" stop-color="var(--grounds-deep)"/>
    </linearGradient>
    <linearGradient id="gold-ring" x1="0" y1="0" x2="1" y2="1">
      <stop offset="0" stop-color="var(--gold-light)"/>
      <stop offset="0.5" stop-color="var(--gold-deep)"/>
      <stop offset="1" stop-color="var(--gold-light)"/>
    </linearGradient>
    <linearGradient id="chevron-tone" x1="0" y1="0" x2="0" y2="1">
      <stop offset="0" stop-color="var(--chevron-tan)" stop-opacity="0.75"/>
      <stop offset="1" stop-color="var(--chevron-tan)" stop-opacity="0.55"/>
    </linearGradient>
    <clipPath id="outer-disc"><circle cx="600" cy="600" r="505"/></clipPath>
    <clipPath id="inner-disc"><circle cx="600" cy="600" r="354"/></clipPath>
  </defs>

  <g class="outer-field" clip-path="url(#outer-disc)">
    <rect class="grounds-photo" role="img" aria-label="Close-up photo of ground coffee" x="95" y="95" width="1010" height="1010" fill="url(#grounds-tone)"/>
    <rect class="lower-band" x="95" y="852" width="1010" height="253" fill="var(--grounds-deep)" opacity="0.45"/>
    <rect class="band-line" x="95" y="846" width="1010" height="6" fill="var(--band-line)"/>
  </g>

  <circle class="gold-frame" cx="600" cy="600" r="361" fill="url(#gold-ring)"/>
  <circle class="label-face" cx="600" cy="600" r="354" fill="var(--label-white)"/>

  <g clip-path="url(#inner-disc)">
    <rect class="chevron-pattern" role="img" aria-label="Tan and white chevron pattern" x="240" y="801" width="720" height="160" fill="url(#chevron-tone)"/>
  </g>

  <text class="tagline" x="846" y="450" text-anchor="end">100% Organic</text>
  <text class="brand-name" x="596" y="648" text-anchor="middle" textLength="498" lengthAdjust="spacingAndGlyphs">MAVU</text>
  <text class="product-type" x="846" y="716" text-anchor="end">BODY SCRUB</text>
</svg>
</body>
</html>
```